Sales Brochure- Generic Line Card 215mm x 140mm

Design a double-sided brochure similar to the attached sample. Cover Page contains a logo and theme that never changes. However, the background picture and the description text on the lower corner will be changed to advertise multiple services. Reverse-side contains Detailed Descriptive text related to the picture on Cover Page as well as Logo and Contact information for the business. Use the Kelvra Controls website www.kelvracontrols.ca for theme, color and contact information. Also, use attached business card design for theme to match. Use the supplied logo. SIZE 215mm x 140mm

Font styles to use
Sans Serif

Colors

Designer to choose colors to be used in the design.

Requirements
Must have
• Look Similar to Sample Brochure but include Kelvra Controls theme and colors

```html
<!DOCTYPE html>
<html lang="en">
<head>
<meta charset="utf-8">
<title>Kelvra Controls – Line Card</title>
<link href="https://fonts.googleapis.com/css2?family=Arimo:wght@400;700&display=swap" rel="stylesheet">
<style>
  :root {
    --ink-deep: #154a4d;
    --teal-text: #1a9b97;
    --accent: #ff4a14;
    --band: #00918f;
    --band-text: #1c474b;
  }
  * { margin: 0; padding: 0; box-sizing: border-box; }
  html, body { width: 1200px; height: 769px; overflow: hidden; }
  body {
    position: relative;
    background: var(--ink-deep);
    font-family: "Arimo", Arial, Helvetica, sans-serif;
    color: var(--teal-text);
  }
  .copy {
    position: absolute;
    left: 78px;
    width: 1070px;
    font-size: 22.4px;
    line-height: 24.6px;
  }
  .copy-services { top: 72px; }
  .copy-location { top: 218px; }
  .copy-clients { top: 364px; }
  .contact {
    position: absolute;
    left: 77px;
    top: 474px;
    font-size: 22.4px;
    line-height: 26px;
    list-style: none;
  }
  .contact li { margin-bottom: 13px; }
  .contact li:nth-child(2) { margin-bottom: 15px; }
  .contact .role, .contact .email, .contact .phone { color: var(--accent); }
  .footer-band {
    position: absolute;
    left: 0; top: 674px;
    width: 1200px; height: 95px;
    background: var(--band);
    border-top: 3px solid var(--accent);
  }
  .brand {
    position: absolute;
    left: 14px; top: 26px;
    display: flex; align-items: center; gap: 12px;
    font-size: 34px; font-weight: 700;
    color: var(--accent);
    letter-spacing: 1px;
  }
  .brand-mark { width: 26px; height: 26px; background: var(--accent); }
  .footer-info {
    position: absolute;
    left: 484px; top: 32px;
    font-size: 22.4px;
    color: var(--band-text);
    white-space: nowrap;
    word-spacing: 1px;
  }
  .footer-info span + span { margin-left: 30px; }
</style>
</head>
<body>
  <p class="copy copy-services">Canada’s only Responsive Machine Shop. Offering production CNC Machining, Swiss Screw Machining, Automated Manufacturing, Robotic Machine Tending, Threading, Prototyping and 24/7 Service, Repair and Welding.</p>
  <p class="copy copy-location">Located in Western Canada, Kelvra Controls is strategically positioned to service energy, oil &amp; gas, mining, architectural and agricultural industries. Our Edmonton based facility is connected to our customers by land, sea and air with export services available to the US and UK.</p>
  <p class="copy copy-clients">We support a large network of diversified clients and pursue new opportunities in all commercial and industrial sectors. Our focus in Responsiveness enables all of our clients to execute their growth initiatives. Contact our Sales Representatives to begin the conversation.</p>

  <ul class="contact">
    <li>Dana Whitlow <span class="role">Manufacturing / Sales</span></li>
    <li class="email">dw@kelvracontrols.ca</li>
    <li class="phone">780.555.0142 x 214</li>
  </ul>

  <footer class="footer-band">
    <div class="brand"><span class="brand-mark"></span>KELVRA CONTROLS</div>
    <div class="footer-info"><span>888.555.0197</span><span>4120 62 Ave NW,&nbsp; Edmonton,&nbsp; AB&nbsp; T6B 2R4</span></div>
  </footer>
</body>
</html>
```